New eyelid plastic surgery office needs a business card design-Eyelid Surgery Partners of Brennor

I recently used SketchHarbor for my logo design and was very pleased with creativity and results. It was a difficult decision for me. Now I would like to create a business card based on this logo, which I will attach.

The text should be easily legible as some of my patients have difficulty seeing, but I would like a subtle, sophisticated artistry also evident to make the card memorable. Would like the card based on a similar color scheme as the logo but the inverse or other complementary colors may prove interesting

A good question was asked...my concern about my visually impaired patients was really my desire to avoid italicized or calligraphic type fonts that may be hard to read. Standard font size for a business card would be fine. Thanks!

Thank you so much for the great work so far. I wanted to give you my particular contact information to see if that would change the look of the cards. Martin Pellowby, MD Address: 2817 Larkmoor Avenue, Suite 205 Wilmington, NC 28517 Phone: 910-555-0183 Fax: 910-555-0184 Website: www.brennorlidclinic.example Please delete the email slot from the card. Thanks so much!

Reason: Last minute consideration. So many great revisions right now!

Plastic

```html
<!DOCTYPE html>
<html lang="en">
<head>
<meta charset="utf-8">
<title>Eyelid Surgery Partners of Brennor — Business Card</title>
<link rel="stylesheet" href="https://fonts.googleapis.com/css2?family=Saira:wght@400;500;600&display=swap">
<style>
  :root {
    --stage: #d9dadb;
    --card-light: #eceeef;
    --card-stripe-zone: #e4e7ea;
    --brand-blue: #1a5fa8;
    --band-blue: #1666b5;
    --ink-white: #ffffff;
    --card-shadow: rgba(0, 0, 0, 0.18);
  }
  * { box-sizing: border-box; margin: 0; padding: 0; }
  html, body {
    width: 1200px; height: 949px; overflow: hidden;
    background: var(--stage);
    font-family: "Saira", "Arial", sans-serif;
  }
  .stage {
    position: relative; width: 1200px; height: 949px;
    display: flex; flex-direction: column; align-items: center; justify-content: center; gap: 72px;
  }
  .card {
    position: relative; width: 640px; height: 366px;
    border-radius: 26px; overflow: hidden;
    background: var(--card-light);
    box-shadow: 0 10px 28px var(--card-shadow);
  }
  .brand-name {
    color: var(--brand-blue); font-weight: 500;
    text-transform: uppercase; letter-spacing: 0.04em; line-height: 1.15;
    font-size: 25px;
  }
  /* Front */
  .card-front .brand-name {
    position: absolute; left: 0; right: 0; top: 120px; text-align: center;
  }
  .card-front .site {
    position: absolute; left: 0; right: 0; top: 262px; text-align: center;
    color: var(--brand-blue); font-size: 17px; letter-spacing: 0.06em;
  }
  /* Back */
  .card-back .top-zone {
    position: absolute; inset: 0 0 auto 0; height: 132px;
    background: var(--card-stripe-zone);
  }
  .card-back .brand-name {
    position: absolute; right: 40px; top: 56px; text-align: right; font-size: 22px;
  }
  .card-back .band {
    position: absolute; left: 0; right: 0; top: 132px; bottom: 0;
    background: var(--band-blue); color: var(--ink-white);
  }
  .holder {
    position: absolute; left: 40px; top: 24px; display: flex; align-items: baseline; gap: 22px;
  }
  .holder-name { font-size: 21px; font-weight: 500; letter-spacing: 0.12em; text-transform: uppercase; }
  .holder-role { font-size: 12px; letter-spacing: 0.12em; text-transform: uppercase; }
  .contact {
    position: absolute; display: flex; align-items: flex-start; gap: 12px;
    font-size: 17px; letter-spacing: 0.05em; line-height: 1.2;
  }
  .contact svg { flex: none; width: 24px; height: 24px; }
  .contact-phone { left: 40px; top: 82px; }
  .contact-email { left: 40px; top: 130px; }
  .contact-address { left: 346px; top: 130px; }
  .contact-web { left: 346px; top: 186px; }
</style>
</head>
<body>
<main class="stage">
  <section class="card card-front" aria-label="Card front">
    <p class="brand-name">Eyelid Surgery Partners<br>of Brennor</p>
    <p class="site">www.yoursite.example</p>
  </section>

  <section class="card card-back" aria-label="Card back">
    <div class="top-zone"></div>
    <p class="brand-name">Eyelid Surgery Partners<br>of Brennor</p>
    <div class="band">
      <div class="holder">
        <span class="holder-name">Alan Corrow</span>
        <span class="holder-role">Founder</span>
      </div>
      <p class="contact contact-phone">
        <svg viewBox="0 0 24 24" aria-hidden="true"><circle cx="12" cy="12" r="10.5" fill="none" stroke="#fff" stroke-width="1.6"/><path d="M9 7.5c-.8.6-1.2 1.6-.9 2.8.6 2.4 2.4 4.4 4.6 5.4 1.1.5 2.2.2 2.8-.6l-1.6-1.6-1.3.7c-1-.5-1.9-1.4-2.4-2.4l.7-1.3z" fill="#fff"/></svg>
        <span>012 555 0147</span>
      </p>
      <p class="contact contact-email">
        <svg viewBox="0 0 24 24" aria-hidden="true"><circle cx="12" cy="12" r="10.5" fill="none" stroke="#fff" stroke-width="1.6"/><rect x="7" y="8.5" width="10" height="7" rx="1" fill="#fff"/><path d="M7.5 9l4.5 3.5L16.5 9" fill="none" stroke="#1666b5" stroke-width="1"/></svg>
        <span>yourname@mail.example</span>
      </p>
      <p class="contact contact-address">
        <svg viewBox="0 0 24 24" aria-hidden="true"><circle cx="12" cy="12" r="10.5" fill="none" stroke="#fff" stroke-width="1.6"/><path d="M12 6.5a3.6 3.6 0 0 0-3.6 3.6c0 2.7 3.6 7 3.6 7s3.6-4.3 3.6-7A3.6 3.6 0 0 0 12 6.5z" fill="#fff"/><circle cx="12" cy="10.1" r="1.3" fill="#1666b5"/></svg>
        <span>041 9th floor Harbor<br>Mews Road LKG</span>
      </p>
      <p class="contact contact-web">
        <svg viewBox="0 0 24 24" aria-hidden="true"><circle cx="12" cy="12" r="10.5" fill="none" stroke="#fff" stroke-width="1.6"/><circle cx="12" cy="12" r="5.5" fill="none" stroke="#fff" stroke-width="1.2"/><ellipse cx="12" cy="12" rx="2.4" ry="5.5" fill="none" stroke="#fff" stroke-width="1"/><path d="M6.5 12h11M7.3 9.2h9.4M7.3 14.8h9.4" stroke="#fff" stroke-width="1"/></svg>
        <span>www.yoursite.example</span>
      </p>
    </div>
  </section>
</main>
</body>
</html>
```